Lantern Square, Steady Course. (Website Design)

We are launching a new bipartisan civic movement: Lantern Square. Steady Course.
The mission is this: Americans deserve a government that is legally required to serve them honestly.
We are looking for a world-class website designer capable of creating an emotionally powerful, modern, cinematic landing page experience that feels larger than politics.
This is not a campaign website for a political party or candidate. We are not looking for a red, white, and blue page with stripes, or American flags, or stock footage of smiling people in a voting booth. We are looking for an emotional and cinematic experience through and through.
The visual direction should feel:
Historic
Hopeful
American
Emotional
Cinematic
Trustworthy
Timeless
The goal is to make visitors feel that they are witnessing the beginning of something important and want to be part of it in the end.
Primary Objective:
Inspire visitors to participate in a one-minute survey and cast their vote.
The survey itself is extremely short and takes approximately one minute to complete.
Everything on the page should ultimately guide visitors toward this action while creating enough curiosity, trust, emotional engagement, and excitement that they feel compelled to take part in the movement.
Audience:
The audience is ordinary Americans across the political spectrum: Democrats, Republicans, Independents.
The design should feel unifying and welcoming.
It should avoid looking partisan, ideological, activist, or government-issued.
Creative Freedom:
We are intentionally giving designers substantial creative freedom.
We are not looking for someone to simply arrange content into predefined sections.
Instead, we are looking for a designer who can think strategically about user experience and persuasion.
The ideal design is as minimal as possible, but you may always:
Use as many sections as you believe are necessary.
Use as many images as you believe are necessary.
Include storytelling elements.
Include data visualizations.
Include timelines.
Include videos.
Include animations.
Include or exclude sections as you see fit.
Reorganize the flow entirely.
We uploaded some files containing text and section suggestions. You don’t have to use them.
We also uploaded some images to convey the general feel we’re looking for.
We are much more interested in the effectiveness of the overall experience than in any specific layout.
What success looks like:
Think outside the box.
Please do not create another generic political website. We have already explored those approaches.
We are looking for something different.
The winning design will be the one that most effectively guides visitors from curiosity to belief to participation.
When a visitor reaches the end of the experience, they should feel:
This is bigger than politics.
This is something I can support regardless of party.
This feels credible.
This feels hopeful.
I want to be part of this.
Use the survey results, the research findings, the principles, the storytelling, or any other elements you believe will help build trust and inspire participation.
Don't just impress us with flashy visuals. Impress us with a website experience that inspires people to become part of the movement and cast their vote.
The final call-to-action should feel like the natural conclusion of the journey, not a request for engagement.
Our goal is not simply to inform visitors. Our goal is to inspire them to cast their vote.
Prioritize emotional impact, storytelling, clarity, and persuasion over decorative design elements.
Final words:
Design a website experience that successfully inspires visitors to take the survey and cast their vote.
Think like a storyteller, not just a designer.
Thank you for your interest in the project.
Best of luck.

```html
<!DOCTYPE html>
<html lang="en">
<head>
<meta charset="utf-8">
<title>Lantern Square. Steady Course.</title>
<link href="https://fonts.googleapis.com/css2?family=Bodoni+Moda:opsz,wght@6..96,400;6..96,500&family=Outfit:wght@300;400;500&display=swap" rel="stylesheet">
<style>
:root{
  --bg:#000;
  --ink:#fff;
  --muted:#cfcfcf;
  --gold:#e9c46c;
  --line:#1c1c1c;
  --card:#050505;
  --card-line:#242424;
  --red:#e0555a;
  --serif:"Bodoni Moda", "Times New Roman", serif;
  --sans:"Outfit", Arial, sans-serif;
}
*{box-sizing:border-box;margin:0;padding:0}
html,body{width:1200px;height:4481px;overflow:hidden;background:var(--bg)}
body{font-family:var(--sans);color:var(--ink)}
.page{position:relative;width:1200px;height:4481px;overflow:hidden;background:var(--bg)}
.abs{position:absolute}
.display{font-family:var(--serif);font-weight:400;text-transform:uppercase;letter-spacing:-0.05em;line-height:1.05}
.center{text-align:center}
.btn{display:flex;align-items:center;justify-content:center;background:var(--gold);color:#111;border-radius:30px;font-size:12px;font-weight:500;letter-spacing:-0.02em}
.rule{height:1px;background:var(--line);left:111px;width:976px}

/* hero */
.hero-art{left:0;top:0;width:1200px;height:713px;
  background:
    linear-gradient(to bottom,rgba(0,0,0,.15) 0%,rgba(0,0,0,0) 30%,rgba(0,0,0,.25) 62%,#000 100%),
    radial-gradient(ellipse 320px 260px at 14% 66%,rgba(196,140,82,.85) 0%,rgba(120,78,44,.4) 45%,rgba(0,0,0,0) 75%),
    radial-gradient(ellipse 380px 300px at 86% 30%,rgba(232,150,90,.9) 0%,rgba(170,80,48,.55) 40%,rgba(0,0,0,0) 78%),
    radial-gradient(ellipse 300px 200px at 58% 6%,rgba(210,196,176,.75) 0%,rgba(150,130,110,.3) 50%,rgba(0,0,0,0) 80%),
    radial-gradient(ellipse 420px 260px at 48% 72%,rgba(150,70,52,.7) 0%,rgba(90,40,34,.35) 50%,rgba(0,0,0,0) 85%),
    radial-gradient(ellipse 260px 200px at 30% 20%,rgba(160,126,96,.55) 0%,rgba(0,0,0,0) 75%),
    linear-gradient(115deg,#4a3322 0%,#5e3f28 35%,#6a3c28 60%,#3d2519 85%,#1c120d 100%)}
.logo{left:111px;top:16px;font-family:var(--serif);font-size:22px;line-height:24px;text-transform:uppercase;letter-spacing:-0.06em}
.header-cta{left:958px;top:21px;width:129px;height:38px;font-size:11px}
.hero-title{left:0;top:196px;width:1200px;font-size:84px;line-height:82px;letter-spacing:-0.06em}
.hero-sub{left:0;top:372px;width:1200px;font-size:12px}
.play{left:546px;top:405px;width:108px;height:108px;border:1.5px solid #fff;border-radius:50%;display:flex;flex-direction:column;align-items:center;justify-content:center;gap:6px;font-size:11px;font-weight:500}
.hero-cta{left:522px;top:537px;width:156px;height:39px}

/* intro */
.hands{left:150px;top:852px;width:420px;height:339px;background:
  radial-gradient(ellipse 150px 110px at 52% 52%,rgba(220,220,220,.85) 0%,rgba(150,150,150,.5) 45%,rgba(0,0,0,0) 100%),
  radial-gradient(ellipse 120px 90px at 25% 30%,rgba(170,170,170,.55) 0%,rgba(0,0,0,0) 100%),
  radial-gradient(ellipse 130px 100px at 78% 72%,rgba(160,160,160,.5) 0%,rgba(0,0,0,0) 100%),
  radial-gradient(ellipse 110px 90px at 80% 22%,rgba(120,120,120,.45) 0%,rgba(0,0,0,0) 100%),
  radial-gradient(ellipse at 50% 50%,#3a3a3a 0%,#141414 70%,#050505 100%)}
.intro-title{left:623px;top:890px;font-size:29px;line-height:37px;width:440px}
.intro-note{left:623px;font-size:11.5px;color:var(--muted)}
.intro-q{left:623px;top:1094px;font-size:18px}

/* movement */
.move-title{left:0;top:1340px;width:1200px;font-size:31px;line-height:38px}
.move-p{left:0;width:1200px;font-size:11.5px;line-height:19px;color:var(--muted)}
.legacy{left:172px;top:1551px;width:856px;height:360px;background:
  linear-gradient(to bottom,rgba(0,0,0,0) 60%,rgba(10,10,14,.55) 100%),
  radial-gradient(ellipse 190px 200px at 28% 40%,rgba(150,120,100,.75) 0%,rgba(90,70,60,.35) 55%,rgba(0,0,0,0) 100%),
  radial-gradient(ellipse 130px 150px at 84% 42%,rgba(210,190,180,.6) 0%,rgba(120,120,140,.25) 55%,rgba(0,0,0,0) 100%),
  radial-gradient(ellipse 120px 70px at 51% 22%,rgba(190,110,110,.5) 0%,rgba(0,0,0,0) 100%),
  linear-gradient(90deg,#2e221d 0%,#4e3b33 30%,#5a5560 55%,#4a5a72 75%,#2c3448 100%)}
.founded{left:758px;top:1812px;width:247px;height:77px;border:1px solid rgba(255,255,255,.5);background:rgba(0,0,0,.35);display:flex;flex-direction:column;align-items:center;justify-content:center;gap:8px}
.founded small{font-size:11px}
.founded b{font-family:var(--serif);font-weight:400;font-size:17px;letter-spacing:-0.05em}

/* cards */
.card{width:307px;border:1px solid var(--card-line);background:var(--card);display:flex;flex-direction:column;align-items:center}
.card .year{font-family:var(--serif);color:var(--gold);font-size:50px;letter-spacing:-0.06em;margin-top:34px;line-height:1}
.card p{font-size:11.5px;line-height:18px;text-align:center;width:225px;margin-top:20px;color:var(--ink)}
.sec-title{left:0;width:1200px;font-size:32px}

/* framework */
.acc{left:128px;width:484px;height:127px;border:1px solid var(--card-line);background:var(--card)}
.acc .num{position:absolute;left:17px;top:40px;font-family:var(--serif);font-size:16px;color:#bbb}
.acc h3{position:absolute;left:61px;top:24px;width:330px;font-family:var(--serif);font-weight:400;font-size:16px;line-height:21px;text-transform:uppercase;letter-spacing:-0.05em}
.acc p{position:absolute;left:61px;font-size:11px;color:var(--muted)}
.acc .plus{position:absolute;right:20px;top:22px;color:var(--gold);font-size:24px;font-weight:300}
.acc-bar{left:113px;width:3px;background:var(--line)}
.capitol{left:657px;top:2754px;width:430px;height:399px;background:
  radial-gradient(ellipse 120px 150px at 50% 58%,rgba(200,200,200,.55) 0%,rgba(0,0,0,0) 100%),
  radial-gradient(ellipse 300px 90px at 50% 85%,rgba(150,150,150,.45) 0%,rgba(0,0,0,0) 100%),
  linear-gradient(180deg,#2a2a2a 0%,#4a4a4a 30%,#6e6e6e 55%,#5a5a5a 80%,#2e2e2e 100%)}

/* stats */
.stat .val{font-family:var(--serif);color:var(--gold);font-size:46px;letter-spacing:-0.06em;margin-top:34px;line-height:1}
.stat .lbl{font-size:11px;margin-top:18px}
.stat .track{width:265px;height:5px;background:#1e1e1e;margin-top:26px;border-radius:3px;overflow:hidden}
.stat .fill{height:100%;background:var(--gold)}
.stress{left:215px;top:3736px;width:770px;font-size:17px;line-height:24px;color:#bfbfbf;font-weight:300;text-align:center}
.party{width:268px;text-align:center}
.party .val{font-family:var(--serif);color:var(--gold);font-size:46px;letter-spacing:-0.06em;line-height:1}
.party .lbl{font-size:11px;margin-top:14px;line-height:26px}
.vline{width:1px;background:var(--line);top:3843px;height:131px}

.final-title{left:0;top:4112px;width:1200px;font-size:32px;line-height:38px}
.final-p{left:0;top:4204px;width:1200px;font-size:11.5px;line-height:19px;color:var(--muted)}
.final-cta{left:494px;top:4274px;width:210px;height:40px}
.footer{left:0;top:4434px;width:1200px;font-size:11px;color:var(--muted)}
</style>
</head>
<body>
<div class="page">

  <div class="abs hero-art" role="img" aria-label="Cinematic sepia scene of a monument statue, soldiers raising a flag and a waving flag at sunset"></div>
  <div class="abs logo">Lantern Square<br>Steady Course</div>
  <div class="abs btn header-cta">Cast Your Vote</div>
  <h1 class="abs display center hero-title">Lantern Square.<br>Steady Course.</h1>
  <p class="abs center hero-sub">Americans deserve a government that is legally required to serve them honestly.</p>
  <div class="abs play">
    <svg width="16" height="18" viewBox="0 0 16 18"><path d="M1 1 L15 9 L1 17 Z" fill="#fff"/></svg>
    <span>Play Video</span>
  </div>
  <div class="abs btn hero-cta">Explore the mission</div>

  <div class="abs hands" role="img" aria-label="Black and white photo of many hands joined together"></div>
  <h2 class="abs display intro-title">Today, not a single<br>law binds our government<br>to act honestly, and in<br>our best interest.</h2>
  <p class="abs intro-note" style="top:1052px">If our government exists solely to serve us,</p>
  <p class="abs display intro-q">Why isn't it legally required to?</p>
  <p class="abs intro-note" style="top:1134px">We founded this movement to change that.</p>

  <div class="abs rule" style="top:1268px"></div>

  <h2 class="abs display center move-title">We are a bipartisan movement based<br>in Washington, D.C.</h2>
  <p class="abs center move-p" style="top:1430px">We believe Americans deserve a government legally required to act honestly, transparently,<br>and in the public's best interest.</p>
  <p class="abs center move-p" style="top:1482px">At a time of growing division and distrust, we are working to unite Americans around a simple idea: government<br>should faithfully serve the people, not special interests.</p>
  <div class="abs legacy" role="img" aria-label="Blended portrait of a historic president, a flag on a ship and a smiling young woman"></div>
  <div class="abs founded"><small>Founded</small><b>2024 • WASHINGTON D.C.</b></div>

  <h2 class="abs display center sec-title" style="top:2004px">What our journey</h2>
  <div class="abs card" style="left:124px;top:2066px;height:200px"><span class="year">2024</span><p>We started a nonprofit with this goal in mind: Americans deserve an honest government.</p></div>
  <div class="abs card" style="left:447px;top:2066px;height:200px"><span class="year">2025</span><p>We identified 10 principles that most of Americans agree our government must uphold.</p></div>
  <div class="abs card" style="left:769px;top:2066px;height:200px"><span class="year">2026</span><p>We turned those principles into a rigorous framework and named it Lantern Square.</p></div>

  <svg class="abs" style="left:550px;top:2345px" width="100" height="100" viewBox="0 0 100 100" aria-hidden="true">
    <g stroke="#2a2212" stroke-width="10">
      <line x1="50" y1="2" x2="50" y2="98"/><line x1="2" y1="50" x2="98" y2="50"/>
      <line x1="16" y1="16" x2="84" y2="84"/><line x1="84" y1="16" x2="16" y2="84"/>
    </g>
  </svg>
  <h2 class="abs display center sec-title" style="top:2458px;line-height:38px">This is bigger than politics. This is<br>about restoring trust.</h2>

  <div class="abs rule" style="top:2601px"></div>

  <h2 class="abs display center sec-title" style="top:2682px">A framework Americans agree on.</h2>
  <div class="abs acc-bar" style="top:2754px;height:399px"></div>
  <div class="abs acc-bar" style="top:2754px;height:127px;background:var(--gold)"></div>
  <div class="abs acc" style="top:2754px"><span class="num">01</span><h3>Public officials should only serve<br>the public good.</h3><p style="top:84px">Not private interests.</p><span class="plus">+</span></div>
  <div class="abs acc" style="top:2890px"><span class="num">02</span><h3>Major government decisions should<br>be based on truth.</h3><p style="top:84px">Not party loyalty, pressure, or donors.</p><span class="plus">+</span></div>
  <div class="abs acc" style="top:3026px"><span class="num">03</span><h3>When a public decision is made people<br>should be able.</h3><p style="top:82px">Clearly. Honestly. On the record.</p><span class="plus">+</span></div>
  <div class="abs capitol" role="img" aria-label="Black and white photo of the Capitol dome under a cloudy sky"></div>

  <div class="abs rule" style="top:3229px"></div>

  <h2 class="abs display center sec-title" style="top:3312px;line-height:38px">82.9% of Americans said yes on a<br>state ballot vote.</h2>
  <p class="abs center move-p" style="top:3400px">We conducted a pre-registered national study with Americans across the political spectrum.<br>We first laid out the 7 principles. We asked if they agree?</p>
  <div class="abs card stat" style="left:124px;top:3476px;height:169px"><span class="val">89.9%</span><span class="lbl">Agree With Principles</span><div class="track"><div class="fill" style="width:83%"></div></div></div>
  <div class="abs card stat" style="left:447px;top:3476px;height:169px"><span class="val">82.9%</span><span class="lbl">Support Legal Framework</span><div class="track"><div class="fill" style="width:72%"></div></div></div>
  <div class="abs card stat" style="left:769px;top:3476px;height:169px"><span class="val">2.7%</span><span class="lbl">Actively Opposed Our Goals</span><div class="track"><div class="fill" style="width:6%;background:var(--red)"></div></div></div>

  <p class="abs stress">But broad support is easy when ideas stay vague. So we stress-tested it. We showed participants<br>the full framework. The legal structure. The enforcement model. The actual mechanism. Most<br>reforms lose support once the details appear. This one didn't. Support held.</p>

  <div class="abs party" style="left:197px;top:3862px"><div class="val">84.5%</div><div class="lbl">Democrats<br>said Yes</div></div>
  <div class="abs vline" style="left:466px"></div>
  <div class="abs party" style="left:466px;top:3862px"><div class="val">80.2%</div><div class="lbl">Republicans<br>said Yes</div></div>
  <div class="abs vline" style="left:734px"></div>
  <div class="abs party" style="left:734px;top:3862px"><div class="val">79.9%</div><div class="lbl">Independents<br>said Yes</div></div>

  <div class="abs rule" style="top:4019px"></div>

  <h2 class="abs display center final-title">We deserve a government legally required<br>to serve the people honestly.</h2>
  <p class="abs center final-p">For decades, we have argued over policies, parties, and ideologies. But today, across political lines,<br>generations, and races, Americans are arriving at the same conclusion. We don't have to<br>ask for it. We just have to vote for it.</p>
  <div class="abs btn final-cta">Be part of history. Vote now.</div>

  <div class="abs rule" style="top:4405px"></div>
  <p class="abs center footer">© 2026 Lantern Square. Steady Course. A bipartisan civic movement. Not affiliated with any party or candidate.</p>
</div>
</body>
</html>
```